new website for ISP and tech consultant

Our company is a wireless Internet Service Provider as well as a technology consultant. We need a new website that is modern looking and something that I can make responsive and mobile friendly. All the pages that are at on our current website (qwelrit.com) must also exist on the new site so please allow space for navigation for them in the design.

It's OK to change logo color

Target Market(s)

Rural internet customers

Industry/Entity Type

Internet Service Provider

Number of Pages Required

1 page

Font styles to use
Sans Serif

Requirements
Must have
• Please keep in mind with the design will need to be able to be made mobile friendly and responsive.
• I'd like an "edge to edge" look in the browser.
• Integrate our logo and the "field" picture (attached)
Should not have
• stock photos (as little as possible)

```html
<!DOCTYPE html>
<html lang="en">
<head>
<meta charset="utf-8">
<title>Qwelrit — Wireless Internet &amp; IT Solutions</title>
<link href="https://fonts.googleapis.com/css2?family=Lato:ital,wght@0,300;0,400;0,700;0,900;1,400&display=swap" rel="stylesheet">
<style>
:root{
  --blue:#2f5fb8;
  --blue-light:#3f7fe0;
  --blue-deep:#1c3f8c;
  --ink:#2b2b2b;
  --text:#444;
  --muted:#666;
  --dark:#1f1f1f;
  --dark-2:#2e2e2e;
  --footer:#1c1c1c;
  --rule:#e4e4e4;
  --field:#eeeeee;
}
*{margin:0;padding:0;box-sizing:border-box}
html,body{width:931px;height:1200px;overflow:hidden;background:#fff}
body{position:relative;font-family:'Lato',sans-serif;color:var(--text)}
.abs{position:absolute}

/* header */
.site-header{left:0;top:0;width:931px;height:67px;background:linear-gradient(#fff,#f1f1f1);border-bottom:2px solid #d6d6d6}
.brand{left:143px;top:14px;display:flex;align-items:center;gap:7px;color:var(--blue);font-weight:900;font-size:19px}
.brand-dot{width:22px;height:22px;border-radius:50%;background:var(--blue)}
.main-nav{right:143px;top:27px;display:flex;gap:9px;font-size:10.5px;color:#444}
.main-nav span+span{margin-left:2px}

/* hero */
.hero{left:0;top:67px;width:931px;height:321px;background:linear-gradient(var(--blue-light),#2a5cbd 55%,var(--blue-deep))}
.hero-title{left:142px;top:48px;color:#fff;font-weight:700;font-size:32px;line-height:41px;text-shadow:0 2px 3px rgba(0,0,0,.25)}
.hero-sub{left:142px;top:175px;color:#fff;font-weight:700;font-size:13.5px}
.btn-join{left:143px;top:205px;width:89px;height:30px;background:#fff;border-radius:2px;color:var(--blue-deep);font-weight:700;font-size:10.5px;display:flex;align-items:center;justify-content:center;box-shadow:0 1px 3px rgba(0,0,0,.3)}
.hero-photo{left:441px;top:21px;width:346px;height:273px;border-radius:6px;background:linear-gradient(135deg,rgba(238,232,220,.55),rgba(90,130,190,.5) 60%,rgba(240,240,240,.5))}

/* features */
.intro{left:142px;top:425px;width:150px}
.intro h2{font-weight:300;font-size:17px;line-height:23.5px;color:#444}
.intro p{font-size:8px;line-height:13.5px;color:#555;margin-top:5px}
.vrule{width:1px;background:var(--rule)}
.feature{width:140px;text-align:center;font-weight:700;font-size:11.5px;line-height:16px;color:#333}
.feature svg{display:block;margin:0 auto 12px}

/* deals */
.deals-title{left:140px;top:588px;font-weight:700;font-size:27px;color:var(--ink);letter-spacing:-.2px}
.deals-sub{left:139px;top:623px;font-weight:700;font-size:13.5px;color:#333}
.deal-input{left:640px;top:592px;width:106px;height:44px;background:var(--field);font-size:10.5px;color:#888;padding:15px 0 0 11px}
.deal-go{left:746px;top:592px;width:42px;height:44px;background:var(--blue);display:flex;align-items:center;justify-content:center}

/* plans */
.plan{top:677px;width:204px;height:141px}
.plan-speed{height:44px;background:var(--dark-2);color:#fff;font-weight:700;font-size:20px;padding:11px 0 0 18px}
.plan-perk{height:51px;background:var(--dark);color:#fff;font-size:10.5px;line-height:17.5px;padding:8px 0 0 18px}
.plan-price{height:46px;background:var(--blue);color:#fff;padding:6px 0 0 17px;font-weight:700;font-size:28px}
.plan-price i{font-weight:400;font-size:17px}

.hrule{left:141px;top:838px;width:648px;height:1px;background:var(--rule)}

/* lower */
.solutions{left:141px;top:855px;width:207px}
.solutions h3{font-weight:700;font-size:20px;color:var(--ink)}
.solutions p{font-size:8px;line-height:13.3px;color:#444;margin-top:7px}
.testimonial-photo{left:141px;top:971px;width:96px;height:66px;background:#ebebeb}
.testimonial{left:245px;top:970px;width:95px;font-size:8px;line-height:10px;color:#333}
.testimonial b{display:block;margin-top:5px;font-size:8px}
.news{left:364px;top:857px;width:195px}
.news h3{font-weight:700;font-size:14px;color:var(--ink)}
.news h4{font-weight:700;font-size:13px;color:#333;margin-top:11px}
.news p{font-size:8px;line-height:13.3px;color:#555;margin-top:2px}
.link-list h3{font-weight:700;font-size:12px;color:var(--ink);margin-bottom:8px}
.link-list li{list-style:none;font-size:8.5px;color:var(--blue);height:23.3px}
.link-list li::before{content:"»";margin-right:5px;font-size:10px}

/* footer */
.site-footer{left:0;top:1064px;width:931px;height:136px;background:var(--footer)}
.foot-brand{left:159px;top:1123px;display:flex;align-items:center;gap:7px;color:#fff;font-weight:900;font-size:19px}
.foot-brand .brand-dot{background:#fff}
.foot-nav{left:278px;top:1100px;display:flex;gap:8px;font-size:10px;color:#ddd}
.foot-rule{left:278px;top:1124px;width:497px;height:1px;background:#555}
.news-label{left:276px;top:1144px;font-size:12.5px;color:#fff}
.foot-input{top:1141px;width:128px;height:24px;background:#f0f0f0;font-size:8px;color:#888;padding:7px 0 0 9px}
.foot-submit{left:672px;top:1141px;width:101px;height:24px;background:var(--blue);color:#fff;font-size:8.5px;font-weight:700;display:flex;align-items:center;justify-content:center}
</style>
</head>
<body>

<header class="site-header abs">
  <div class="brand abs"><span class="brand-dot"></span>Qwelrit</div>
  <nav class="main-nav abs"><span>Home</span><span>Internet</span><span>Services</span><span>Products</span><span>Pay your bill</span><span>Email</span><span>Support</span><span>Contact</span><span>News</span></nav>
</header>

<section class="hero abs">
  <h1 class="hero-title abs">High-Speed wireless<br>Internet starting at<br>$49.95/month</h1>
  <p class="hero-sub abs">NO arbitrary data cap! * No hidden fees!</p>
  <div class="btn-join abs">Join Now</div>
  <div class="hero-photo abs" role="img" aria-label="Photo of a young man sitting on the floor using a laptop"></div>
</section>

<div class="intro abs">
  <h2>Fast download &amp; upload speeds at an affordable price</h2>
  <p>Praesent vestibulum aenean nonummy hendrerit mauris. Cum sociis natoque penatibus et magnis dis parturient montes ascetur ridiculus mus. Nulla dui.</p>
</div>
<div class="vrule abs" style="left:299px;top:427px;height:123px"></div>
<div class="vrule abs" style="left:463px;top:447px;height:75px"></div>
<div class="vrule abs" style="left:632px;top:447px;height:75px"></div>

<div class="feature abs" style="left:314px;top:440px">
  <svg width="52" height="46" viewBox="0 0 52 46" fill="#2f5fb8">
    <circle cx="17" cy="24" r="12"/><circle cx="17" cy="24" r="5" fill="#fff"/>
    <g stroke="#2f5fb8" stroke-width="5"><line x1="17" y1="8" x2="17" y2="40"/><line x1="1" y1="24" x2="33" y2="24"/><line x1="6" y1="13" x2="28" y2="35"/><line x1="28" y1="13" x2="6" y2="35"/></g>
    <circle cx="17" cy="24" r="5" fill="#fff"/>
    <circle cx="40" cy="10" r="7"/><circle cx="40" cy="10" r="2.5" fill="#fff"/>
    <circle cx="40" cy="36" r="7"/><circle cx="40" cy="36" r="2.5" fill="#fff"/>
  </svg>
  Equipment Installation<br>and Setup
</div>
<div class="feature abs" style="left:478px;top:428px">
  <svg width="54" height="58" viewBox="0 0 54 58" fill="none" stroke="#2f5fb8" stroke-width="4">
    <path d="M9 30 A18 18 0 0 1 45 30"/>
    <circle cx="27" cy="30" r="15"/>
    <rect x="4" y="26" width="8" height="14" rx="3" fill="#2f5fb8"/>
    <rect x="42" y="26" width="8" height="14" rx="3" fill="#2f5fb8"/>
    <path d="M46 40 Q44 50 32 50"/>
  </svg>
  Castomer Support<br>Center
</div>
<div class="feature abs" style="left:644px;top:442px">
  <svg width="44" height="44" viewBox="0 0 44 44" fill="#2f5fb8">
    <rect x="2" y="18" width="10" height="22" rx="1"/>
    <path d="M15 18 L24 4 Q29 2 29 9 L27 16 L38 16 Q43 17 41 23 L37 38 Q35 42 30 42 L15 42 Z"/>
  </svg>
  Customer<br>Guarantee
</div>

<h2 class="deals-title abs">FIND THE BEST DEALS IN YOUR AREA</h2>
<p class="deals-sub abs">ENTER YOUR PLANS AND GET PRICE DETAILES</p>
<div class="deal-input abs">Enter Here</div>
<div class="deal-go abs"><svg width="10" height="14" viewBox="0 0 10 14"><path d="M1 0 L10 7 L1 14 Z" fill="#fff"/></svg></div>

<div class="plan abs" style="left:142px">
  <div class="plan-speed">2 Mbps</div>
  <div class="plan-perk">ACCESS TO 100,000 WIFI<br>HOTSPOTS AT NO EXTRA COST</div>
  <div class="plan-price">$25.99/<i>Month</i></div>
</div>
<div class="plan abs" style="left:364px">
  <div class="plan-speed">5 Mbps</div>
  <div class="plan-perk">ACCESS TO 100,000 WIFI<br>HOTSPOTS AT NO EXTRA COST</div>
  <div class="plan-price">$45.99/<i>Month</i></div>
</div>
<div class="plan abs" style="left:585px">
  <div class="plan-speed">10 Mbps</div>
  <div class="plan-perk">ACCESS TO 100,000 WIFI<br>HOTSPOTS AT NO EXTRA COST</div>
  <div class="plan-price">$65.99/<i>Month</i></div>
</div>

<div class="hrule abs"></div>

<div class="solutions abs">
  <h3>NEED IT SOLUTIONS?</h3>
  <p>Lorem ipsum dolor sit amet, consectetur adipisicing elit, sed do eiusmod tempor incididunt ut labore et dolore magna aliqua. Ut enim ad minim veniam, quis nostrud exercitation ullamco laboris nisi ut aliquip commodo consequat. Duis aute irure dolor in reprehenderit in voluptate velit esse.</p>
</div>
<div class="testimonial-photo abs" role="img" aria-label="Portrait photo of the quoted director"></div>
<div class="testimonial abs">“ Aenean nonummy hendrerit mau phasellu porta. Fusce Aenean nonummy hendrerit mau phasellu porta.”<b>Dale Morrowdirector</b></div>

<div class="news abs">
  <h3>NEWS &amp; EVENTS:</h3>
  <h4>03/14</h4>
  <p>laboris nisi ut aliquip commodo consequat. Duis aute irure dolor in reprehenderit in voluptate velit esse. laboris nisi ut aliquip commodo consequat. Duis aute irure dolor in reprehenderit in voluptate velit esse.</p>
  <h4>03/14</h4>
  <p>laboris nisi ut aliquip commodo consequat. Duis aute irure dolor in reprehenderit in voluptate velit esse. laboris nisi ut aliquip commodo consequat. Duis aute irure dolor in reprehenderit in voluptate velit esse.</p>
</div>

<div class="link-list abs" style="left:584px;top:856px">
  <h3>FEATURED:</h3>
  <ul><li>Managed Services</li><li>Virtual Office</li><li>Strategic Planning</li><li>Installation</li><li>Mobile IT</li><li>Network Security</li></ul>
</div>
<div class="link-list abs" style="left:695px;top:856px">
  <h3>POPULAR:</h3>
  <ul><li>Managed Services</li><li>Virtual Office</li><li>Strategic Planning</li><li>Installation</li><li>Mobile IT</li><li>Network Security</li></ul>
</div>

<footer class="site-footer abs"></footer>
<div class="foot-brand abs"><span class="brand-dot"></span>Qwelrit</div>
<nav class="foot-nav abs"><span>Home</span><span>Internet</span><span>Services</span><span>Products</span><span>Pay your bill</span><span>Email</span><span>Support</span><span>Contact</span><span>News</span></nav>
<div class="foot-rule abs"></div>
<div class="news-label abs">Signup Newslatter</div>
<div class="foot-input abs" style="left:390px">Enter Name</div>
<div class="foot-input abs" style="left:531px">Enter Email</div>
<div class="foot-submit abs">SUBMIT</div>

</body>
</html>
```